Lorne Hollow Farm Postcard Design

I am looking for a new postcard design to mail out this season. We are a Farm business that does wholesale and retail and bulk seasoned firewood sales. we sell firewood from anything from bagged wood to tractor trailer loads of wood. We sell firewood in bulk bags. Pick up or delivery available there is no order to big or too small. I need my business name and phone number on the cards Lorne Hollow Farm 848-316-0572 (call or text) I would like it to say we are the best priced guaranteed. I want something that is simple and straight forward but also really catches the eye when they see these in the mail box. I attached my logo and feel free to use photos of split firewood if you would like. id like my email on the card Lornehollowfarm90@mailvista.net.

Target Market(s)

Firewood purchasers

Industry/Entity Type

agriculture

Requirements
Must have
• email phone number logo

```html
<!DOCTYPE html>
<html lang="en">
<head>
<meta charset="utf-8">
<title>Lorne Hollow Farm Postcard</title>
<link href="https://fonts.googleapis.com/css2?family=Oswald:wght@400;500;600&display=swap" rel="stylesheet">
<style>
  :root {
    --scene-bg: #2a0608;
    --card-black: #0a0605;
    --band-maroon: #7a0f17;
    --fire-core: #ffb347;
    --fire-mid: #c2410c;
    --fire-dark: #3a120a;
    --hot-red: #ff3b1f;
    --hot-orange: #ff8a1c;
    --gold: #ffc21a;
    --white: #ffffff;
  }
  * { margin: 0; padding: 0; box-sizing: border-box; }
  html, body {
    width: 828px; height: 1200px; overflow: hidden;
    background: var(--scene-bg);
    font-family: "Oswald", "Arial Narrow", sans-serif;
  }
  .postcard {
    position: absolute; left: 0; top: 324px;
    width: 828px; height: 552px;
    background: var(--card-black);
    overflow: hidden;
  }
  .campfire-photo {
    position: absolute; left: 0; top: 0; width: 828px; height: 486px;
    background:
      radial-gradient(ellipse 90px 150px at 415px 200px, var(--fire-core) 0%, rgba(255,140,40,.75) 35%, rgba(0,0,0,0) 100%),
      radial-gradient(ellipse 260px 170px at 420px 330px, var(--fire-mid) 0%, var(--fire-dark) 55%, rgba(0,0,0,0) 100%),
      linear-gradient(180deg, #050303 0%, #1a0805 60%, #2b0d07 100%);
  }
  .bottom-band {
    position: absolute; left: 0; top: 486px; width: 828px; height: 66px;
    background: var(--band-maroon);
  }
  .brand {
    position: absolute; left: 28px; top: 40px;
    display: flex; align-items: center; gap: 12px;
  }
  .brand-mark { width: 22px; height: 22px; background: var(--hot-orange); }
  .brand-name {
    font-weight: 600; font-size: 40px; line-height: 1;
    color: var(--hot-orange); text-transform: uppercase; letter-spacing: 1px;
  }
  .contact {
    position: absolute; right: 22px; top: 30px; text-align: right; color: var(--white);
  }
  .contact-label { font-size: 22px; font-weight: 400; line-height: 1.1; }
  .contact-phone {
    font-size: 48px; font-weight: 600; line-height: 1.05; letter-spacing: 1px;
    color: var(--hot-orange);
  }
  .contact-email { font-size: 17px; font-weight: 400; letter-spacing: .5px; text-transform: uppercase; }
  .headline {
    font-weight: 500; font-size: 40px; line-height: 1.12; text-transform: uppercase;
    -webkit-background-clip: text; background-clip: text; color: transparent;
  }
  .offer-left { position: absolute; left: 24px; top: 240px; }
  .offer-left .headline { background-image: linear-gradient(90deg, var(--hot-red), var(--hot-orange) 80%); }
  .offer-right { position: absolute; right: 33px; top: 238px; text-align: right; }
  .offer-right .headline { background-image: linear-gradient(90deg, var(--hot-orange), var(--gold)); }
  .rule { height: 4px; width: 124px; background: var(--white); margin: 10px 0 14px; }
  .offer-right .rule { margin-left: auto; }
  .subline { color: var(--white); font-size: 22px; line-height: 1.3; text-transform: uppercase; font-weight: 400; }
  .photo-strip { position: absolute; left: 0; top: 442px; width: 828px; height: 84px; }
  .strip-photo {
    position: absolute; top: 0; height: 84px;
    border: 4px solid var(--white);
    transform: skewX(-14deg);
  }
  .strip-loader { left: 44px; width: 228px; background: linear-gradient(180deg, #6f9a4a 0%, #9aa06a 45%, #b59a5c 100%); }
  .strip-logs { left: 292px; width: 228px; background: linear-gradient(180deg, #8aa04c 0%, #7a4a2a 55%, #c78a4a 100%); }
  .strip-split { left: 540px; width: 250px; background: linear-gradient(135deg, #e6b27a 0%, #c9814a 50%, #7a3f1f 100%); }
</style>
</head>
<body>
  <main class="postcard">
    <div class="campfire-photo" role="img" aria-label="Photo of a campfire burning at night on red earth"></div>
    <div class="bottom-band"></div>

    <div class="brand">
      <span class="brand-mark"></span>
      <span class="brand-name">Lorne Hollow Farm</span>
    </div>

    <div class="contact">
      <p class="contact-label">CALL OR TEXT</p>
      <p class="contact-phone">848 316 0572</p>
      <p class="contact-email">Lornehollowfarm90@mailvista.net</p>
    </div>

    <section class="offer-left">
      <h2 class="headline">No order too big<br>or too small</h2>
      <div class="rule"></div>
      <p class="subline">From bagged wood to<br>tractor trailer loads of wood</p>
    </section>

    <section class="offer-right">
      <h2 class="headline">Best prices<br>guaranteed</h2>
      <div class="rule"></div>
      <p class="subline">Not your average<br>firewood for sale.</p>
    </section>

    <div class="photo-strip">
      <div class="strip-photo strip-loader" role="img" aria-label="Photo of a yellow log loader moving timber"></div>
      <div class="strip-photo strip-logs" role="img" aria-label="Photo of cut logs lying on the ground"></div>
      <div class="strip-photo strip-split" role="img" aria-label="Photo of stacked split firewood"></div>
    </div>
  </main>
</body>
</html>
```